Business card design needed

I need a simple business card design with contact details on one side (and a logo) and 2 logos on the other side. I would like the text to be in silver and the card black.

Target Market(s)

Luxury market

Industry/Entity Type

Business

Contact Information for Business Card

M&K Forvela, PO BOX 517, Brindlecoe, VIC, 3186

Logo Text

M&K Forvela

Requirements
Must have
• black card, 2 logos on back, M&K logo on front

Text on front should be

Neil & Priya Haverstock

Neil 0417826391 Priya 0428650147
neil@mkforvela.com priya@mkforvela.com
PO BOX 517, Brindlecoe, VIC, 3186

```html
<!DOCTYPE html>
<html lang="en">
<head>
<meta charset="utf-8">
<title>M&amp;K Forvela – Business Card</title>
<link rel="stylesheet" href="https://fonts.googleapis.com/css2?family=Lobster&family=Quicksand:wght@500&display=swap">
<style>
  :root {
    --card-black: #1d1d1d;
    --card-deep: #141414;
    --panel-black: #0d0d0d;
    --panel-edge: #2a2a2a;
    --silver: #ededed;
    --silver-soft: #d8d8d8;
    --logo-grey: #3b3b3b;
  }
  * { margin: 0; padding: 0; box-sizing: border-box; }
  html, body {
    width: 1200px;
    height: 741px;
    overflow: hidden;
    background: var(--card-black);
  }
  .card {
    position: relative;
    width: 1200px;
    height: 741px;
    overflow: hidden;
    background: var(--card-black);
    font-family: "Quicksand", sans-serif;
    color: var(--silver);
  }
  .card-texture {
    position: absolute;
    inset: 0;
    background:
      radial-gradient(ellipse at 25% 80%, rgba(60,60,60,0.35), transparent 55%),
      radial-gradient(ellipse at 85% 30%, rgba(55,55,55,0.3), transparent 50%),
      linear-gradient(160deg, #222 0%, var(--card-black) 50%, var(--card-deep) 100%);
  }
  .panels {
    position: absolute;
    inset: 0;
  }
  .logo-tile {
    position: absolute;
    left: 150px;
    top: 93px;
    width: 273px;
    height: 225px;
    border-radius: 22px;
    background: linear-gradient(180deg, #0b0b0b, #111);
  }
  .brand-name {
    position: absolute;
    left: 150px;
    top: 343px;
    width: 273px;
    text-align: center;
    font-size: 30px;
    font-weight: 500;
    color: var(--logo-grey);
  }
  .script {
    font-family: "Lobster", cursive;
    font-weight: 400;
  }
  .address-block {
    position: absolute;
    right: 132px;
    top: 92px;
    text-align: right;
  }
  .owners {
    font-size: 40px;
    line-height: 1;
    margin-bottom: 14px;
  }
  .postal {
    font-size: 37px;
    line-height: 54px;
    color: var(--silver-soft);
  }
  .contact {
    position: absolute;
    top: 565px;
    font-size: 30px;
    line-height: 43px;
    color: var(--silver);
  }
  .contact-neil { left: 175px; }
  .contact-priya { right: 154px; text-align: right; }
  .contact .first-name {
    font-size: 39px;
    margin-right: 6px;
  }
</style>
</head>
<body>
<main class="card">
  <div class="card-texture" role="img" aria-label="Faint dark flourish pattern across the card background"></div>

  <svg class="panels" width="1200" height="741" viewBox="0 0 1200 741" aria-hidden="true">
    <path d="M503 83 L1200 22 L1200 285 L555 370 Z" fill="var(--panel-black)" stroke="var(--panel-edge)" stroke-width="2" stroke-linejoin="round"/>
    <path d="M102 528 L1102 465 L1115 741 L115 741 Z" fill="var(--panel-black)" stroke="var(--panel-edge)" stroke-width="2" stroke-linejoin="round"/>
  </svg>

  <div class="logo-tile" aria-hidden="true"></div>
  <div class="brand-name">M&amp;K Forvela</div>

  <section class="address-block">
    <p class="owners script">Neil &amp; Priya Haverstock</p>
    <p class="postal">PO BOX 517, Brindlecoe,<br>VIC, 3186</p>
  </section>

  <section class="contact contact-neil">
    <p><span class="first-name script">Neil</span> 0417826391</p>
    <p>neil@mkforvela.com</p>
  </section>

  <section class="contact contact-priya">
    <p><span class="first-name script">Priya</span> 0428650147</p>
    <p>priya@mkforvela.com</p>
  </section>
</main>
</body>
</html>
```